Gentle Kundalini Yoga with Gong Relaxation

I teach a gentle Kundalini Yoga class with Gong relaxation every Thursday morning from 8:30-10am at the Ashford Meadows Unity Chapel 17 Garber Lane Pellam Crest. This class is unique in that I play the gong for an extended relaxation. Gongs are generally only found in established Yoga centers not in a small neighborhood yoga class. I am trying to grow this class from a current class size of 5 students. I would like to double the class size.
Updates
Project Deadline Extended
Reason: We had a blizzard on January 27 and 28 in the Boston area and I was too busy removing snow to tend to the postcard design-Thank you-Dora Fitchley
Industry/Entity Type
Church

```html
<!DOCTYPE html>
<html lang="en">
<head>
<meta charset="utf-8">
<title>Gentle Kundalini Yoga with Gong Relaxation</title>
<link href="https://fonts.googleapis.com/css2?family=Open+Sans:wght@300;400;600;700;800&display=swap" rel="stylesheet">
<style>
  :root {
    --page: #e9ebee;
    --card-light: #f4f9fd;
    --card-mid: #d6e8f6;
    --card-edge: #a9cbe7;
    --ink: #3b4148;
    --ink-soft: #5a646e;
    --ribbon: #3f8fcf;
    --ribbon-dark: #1f5f96;
    --badge: #2e86cc;
    --rule: #7f8a95;
    --photo-warm: #c9a98c;
    --photo-light: #efe6dc;
    --white: #ffffff;
  }
  * { margin: 0; padding: 0; box-sizing: border-box; }
  html, body { width: 1200px; height: 771px; overflow: hidden; }
  body {
    background: var(--page);
    font-family: "Open Sans", Arial, sans-serif;
    position: relative;
  }
  .postcard {
    position: absolute;
    left: 80px; top: 45px;
    width: 1040px; height: 680px;
    background: radial-gradient(ellipse at 28% 45%, var(--card-light) 0%, var(--card-mid) 55%, var(--card-edge) 100%);
    box-shadow: 0 6px 22px rgba(0,0,0,0.18);
    overflow: hidden;
  }
  .title-block { position: absolute; left: 40px; top: 112px; }
  .title {
    font-size: 34px; font-weight: 800; color: var(--ink);
    letter-spacing: 1px; line-height: 1;
  }
  .subtitle {
    font-size: 17px; font-weight: 300; color: var(--ink-soft);
    letter-spacing: 3px; margin-top: 6px; padding-left: 52px;
  }
  .meditation-art {
    position: absolute; left: 70px; top: 175px;
    width: 360px; height: 320px;
    border-radius: 50% 50% 40% 40%;
    background: radial-gradient(ellipse at 50% 45%, #ffffff 0%, #a7d0f0 30%, #4f8cc4 60%, rgba(79,140,196,0) 75%);
  }
  .ribbon { position: absolute; left: 30px; top: 408px; width: 470px; height: 110px; }
  .ribbon svg { position: absolute; inset: 0; }
  .ribbon-left, .ribbon-right {
    position: absolute; color: var(--white); font-size: 14px; line-height: 1.12;
    text-align: center; width: 170px;
  }
  .ribbon-left { left: 32px; top: 30px; }
  .ribbon-right { left: 292px; top: 14px; }
  .ribbon strong { font-weight: 700; color: #e8f4ff; }
  .price-badge {
    position: absolute; left: 203px; top: 14px;
    width: 86px; height: 86px; border-radius: 50%;
    background: var(--badge); border: 4px solid var(--white);
    box-shadow: 0 2px 6px rgba(0,0,0,0.3);
    color: var(--white); text-align: center;
    display: flex; flex-direction: column; justify-content: center;
  }
  .price-badge .count { font-size: 13px; }
  .price-badge .amount { font-size: 27px; font-weight: 700; line-height: 1; }
  .address-block {
    position: absolute; left: 40px; top: 550px;
    font-size: 14px; font-style: normal; color: var(--ink-soft); line-height: 1.45;
  }
  .address-block b { color: var(--ink); }
  .address-line2 { padding-left: 150px; }
  .contact-line { margin-top: 10px; }
  .intro { position: absolute; left: 530px; top: 105px; width: 450px; }
  .rule { display: block; width: 100%; height: 10px; }
  .intro-text {
    font-size: 11.5px; font-weight: 700; color: var(--ink);
    text-align: center; line-height: 1.55; margin: 10px 0 12px;
  }
  .intro-text p + p { margin-top: 10px; }
  .photo-area { position: absolute; left: 520px; top: 320px; width: 520px; height: 360px; }
  .photo-area svg { position: absolute; inset: 0; }
  .quote {
    position: absolute; left: 620px; top: 530px; width: 400px;
    color: var(--white); font-size: 14px; font-weight: 600; text-align: center;
    line-height: 1.35; text-shadow: 0 1px 3px rgba(0,0,0,0.5);
  }
  .quote cite { display: block; font-style: normal; text-align: right; padding-right: 30px; }
</style>
</head>
<body>
<main class="postcard">
  <header class="title-block">
    <h1 class="title">GENTLE KUNDALINI YOGA</h1>
    <p class="subtitle">WITH GONG RELAXATION</p>
  </header>

  <div class="meditation-art" role="img" aria-label="Glowing blue silhouette of a person meditating in lotus pose before a lotus flower outline"></div>

  <section class="ribbon">
    <svg viewBox="0 0 470 110" aria-hidden="true">
      <polygon points="0,42 30,42 22,70 30,98 0,98 10,70" fill="var(--ribbon-dark)"/>
      <polygon points="470,14 440,14 448,40 440,68 470,68 460,41" fill="var(--ribbon-dark)"/>
      <polygon points="20,24 450,4 450,84 20,104" fill="var(--ribbon)"/>
    </svg>
    <div class="ribbon-left"><strong>Trainer:</strong><br>Dora Fitchley<br><strong>Dates:</strong><br>Thursdays 8:30-10am</div>
    <div class="price-badge"><span class="count">10 Classes</span><span class="amount">$100</span></div>
    <div class="ribbon-right"><strong>Call:</strong><br>555-014-2388<br><strong>Email:</strong><br>hello@ashfordyoga.org</div>
  </section>

  <address class="address-block">
    <div><b>Address:</b> Ashford Meadows Unity Chapel 17 Garber Lane</div>
    <div class="address-line2">Pellam Crest, Massachusetts.</div>
    <div class="contact-line"><b>Website:</b> ashfordyoga.org &nbsp;|&nbsp; <b>Social:</b> /ashfordyoga &nbsp;|&nbsp; <b>Updates:</b> /ashfordnews</div>
  </address>

  <section class="intro">
    <svg class="rule" viewBox="0 0 450 10" preserveAspectRatio="none" aria-hidden="true">
      <line x1="0" y1="5" x2="438" y2="5" stroke="var(--rule)" stroke-width="1"/>
      <circle cx="443" cy="5" r="3" fill="none" stroke="var(--rule)"/>
    </svg>
    <div class="intro-text">
      <p>Kundalini Yoga is called the Yoga of Awareness. It is a dynamic, powerful tool that is designed to give you an experience of your soul.</p>
      <p>In Kundalini Yoga we harness the mental, physical, and nervous energies of the body and put them under the domain of the will, which is the instrument of the soul. This technology precisely and consciously combines breath, mudra, eye focus, mantra, body locks, and postures to balance the glandular system, strengthen the nervous system, expand lung capacity, and purify the blood. It brings balance to the body, mind, and soul.</p>
    </div>
    <svg class="rule" viewBox="0 0 450 10" preserveAspectRatio="none" aria-hidden="true">
      <circle cx="7" cy="5" r="3" fill="none" stroke="var(--rule)"/>
      <line x1="12" y1="5" x2="450" y2="5" stroke="var(--rule)" stroke-width="1"/>
    </svg>
  </section>

  <div class="photo-area">
    <svg viewBox="0 0 520 360" aria-hidden="true">
      <defs>
        <linearGradient id="photoTone" x1="0" y1="0" x2="1" y2="1">
          <stop offset="0" stop-color="var(--photo-light)"/>
          <stop offset="0.5" stop-color="var(--photo-warm)"/>
          <stop offset="1" stop-color="#8a6d57"/>
        </linearGradient>
      </defs>
      <path d="M520,0 L520,360 L140,360 C40,330 20,230 70,140 C130,40 300,5 520,0 Z" fill="var(--white)" opacity="0.85"/>
      <path d="M520,12 L520,360 L160,360 C60,325 45,235 92,152 C150,58 310,18 520,12 Z" fill="url(#photoTone)" role="img" aria-label="Soft photo of a woman in white seated cross-legged meditating"/>
    </svg>
  </div>
  <blockquote class="quote">
    “Kundalini Yoga is the science to unite the finite with Infinity, and it's the art to experience Infinity in the finite.”
    <cite>-Teacher Anand Varo, 10/27/88</cite>
  </blockquote>
</main>
</body>
</html>
```